Verdell Chiropractic, achieve your health goals, get better each day one step at a time

A mobile friendly site, fresh look, easy to navigate, has interface with pw/chirply, etc. Blog posts. Uses new logo. Content and address to current site is mirvaton.com. The current site will give you scope of project for content. The logo is not the final but close. Will upload final next week.
Convey the concept that heath is a process, it does not just happen. We take steps to achieve what we want in life including health.

Target Market(s)

30 to 70 year old. Needing health care

Industry/Entity Type

Health Care

Coding

Coded - Design and coding required

Number of Pages Required

5+ page

Font styles to use
Sans Serif

Colors

Designer to choose colors to be used in the design.

Requirements
Must have
• mobile friendly, easy to navigate, PW/Chirply interface, blog, room for current content
Nice to have
• potential for commerce, statistics
Should not have
• Same old look and feel as everything else out there

```html
<!DOCTYPE html>
<html lang="en">
<head>
<meta charset="utf-8">
<title>Verdell Chiropractic</title>
<link rel="stylesheet" href="https://fonts.googleapis.com/css2?family=Oswald:wght@500;600&family=Questrial&display=swap">
<style>
:root{
  --blue:#2f7fc1;
  --blue-band:#3683c2;
  --blue-dark:#2a74b2;
  --green:#8dc63f;
  --ink:#444a50;
  --muted:#6b7075;
  --white:#ffffff;
  --line:#9aa0a6;
}
*{box-sizing:border-box;margin:0;padding:0}
html,body{width:1200px;height:3297px;overflow:hidden}
body{position:relative;background:var(--white);font-family:"Questrial",Arial,sans-serif;color:var(--ink)}
.abs{position:absolute}
.center{text-align:center;left:0;width:1200px}
.heading{font-family:"Oswald",Impact,sans-serif;font-weight:600;letter-spacing:1px;color:var(--blue);font-size:48px;line-height:1}
.heading.light{color:var(--white)}
.tagline{font-size:15px;color:var(--green)}
.btn-outline{border:1.5px solid var(--line);color:var(--ink);font-size:15px;display:flex;align-items:center;justify-content:center;background:var(--white)}

/* header */
.topbar{left:440px;top:0;width:760px;height:24px;background:var(--blue);border-bottom-left-radius:24px;color:var(--white);font-size:13px;display:flex;align-items:center;gap:42px;padding-left:72px}
.topbar span{display:flex;align-items:center;gap:8px}
.topbar .social{margin-left:auto;margin-right:28px;gap:14px;font-size:12px}
.brand{left:88px;top:30px;font-size:26px;color:var(--blue);display:flex;align-items:center;gap:10px;letter-spacing:.5px}
.brand .mark{width:22px;height:22px;border-radius:50%;background:var(--green)}
.nav{left:360px;top:45px;display:flex;gap:22px;font-size:15px;color:var(--ink)}
.cta{left:895px;top:37px;width:219px;height:38px;background:var(--green);color:var(--white);font-size:16px;display:flex;align-items:center;justify-content:center}

/* hero */
.hero{left:0;top:88px;width:1200px;height:422px;background:linear-gradient(110deg,#c9c2bb 0%,#e6e2dd 35%,#cfd7de 60%,#6f93b6 85%,#3f73a8 100%)}
.hero-title{top:240px;font-family:"Oswald",Impact,sans-serif;font-weight:500;font-size:66px;color:var(--white);letter-spacing:2px}
.hero-sub{left:280px;top:320px;width:644px;height:28px;background:rgba(70,70,70,.55);color:var(--white);font-size:18px;letter-spacing:1px;display:flex;align-items:center;justify-content:center}
.dots{display:flex;gap:6px;justify-content:center}
.dots i{width:9px;height:9px;border-radius:50%;background:rgba(255,255,255,.6)}
.dots i:first-child{background:var(--white)}

/* about */
.about-title{left:130px;top:600px}
.about-lead{left:130px;top:660px;width:420px;font-size:15px;line-height:26px;color:var(--green)}
.about-body{left:130px;top:722px;width:420px;font-size:14px;line-height:24px;color:var(--muted)}
.about-btn{left:130px;top:858px;width:147px;height:39px}
.about-photo{left:591px;top:589px;width:479px;height:334px;background:linear-gradient(135deg,#d8dfe4,#f1f3f4 50%,#b9c6cf);box-shadow:0 6px 22px rgba(0,0,0,.25)}

/* conditions */
.conditions{left:0;top:989px;width:1200px;height:580px;background:var(--blue-band)}
.cond-intro{top:1126px;font-size:14px;color:var(--white);letter-spacing:.3px}
.cond-grid{left:86px;top:1160px;display:grid;grid-template-columns:repeat(5,198px);column-gap:10px;row-gap:49px}
.cond-tile{width:198px}
.cond-tile .ph{height:130px}
.cond-tile p{margin-top:10px;text-align:center;color:var(--white);font-size:14px;letter-spacing:1px}

/* services */
.services-tag{top:1712px}
.svc{top:1762px;width:140px;text-align:center;font-size:14px;line-height:21px;letter-spacing:1px;color:var(--ink)}
.svc svg{display:block;margin:0 auto 10px}

/* testimonial */
.testimonial{left:0;top:1978px;width:1200px;height:418px;background:linear-gradient(180deg,#6d8a5a 0%,#8aa47a 40%,#7e8d86 70%,#5e6f7a 100%)}
.quote-mark{top:2052px;font-family:"Oswald",Impact,sans-serif;font-size:110px;line-height:1;color:rgba(255,255,255,.9)}
.quote{left:240px;top:2137px;width:720px;text-align:center;font-style:italic;font-size:16px;line-height:26px;color:var(--white)}
.quote-by{top:2254px;font-size:15px;color:var(--white);font-weight:bold}

/* blog */
.blog-tag{top:2538px}
.card{top:2585px;width:325px}
.card .ph{height:220px;position:relative}
.card .date{position:absolute;left:0;bottom:0;width:48px;height:57px;background:var(--green);color:var(--white);font-size:13px;line-height:17px;padding:10px 0 0 7px}
.card h3{margin:20px 0 0 8px;font-weight:normal;font-size:20px;color:var(--blue)}
.card p{margin:12px 0 0 8px;width:300px;font-size:14px;line-height:23px;color:var(--muted)}
.card .btn-outline{margin:14px 0 0 8px;width:145px;height:36px}

/* footer */
.footer{left:0;top:3066px;width:1200px;height:196px;background:var(--blue-dark)}
.foot-brand{left:88px;top:3148px;font-size:22px;color:var(--white);display:flex;align-items:center;gap:10px}
.foot-brand .mark{width:18px;height:18px;border-radius:50%;background:var(--green)}
.vline{top:3120px;width:1px;height:100px;background:rgba(255,255,255,.25)}
.foot-h{font-size:12px;color:var(--green);letter-spacing:1px}
.foot-list{font-size:11px;line-height:20px;color:var(--white)}
.bottombar{left:0;top:3262px;width:1200px;height:35px;background:var(--green);color:var(--white);font-size:11px;display:flex;align-items:center;padding:0 88px}
.bottombar .social{margin-left:auto;display:flex;gap:14px}
</style>
</head>
<body>

<!-- header -->
<div class="abs topbar">
  <span><svg width="12" height="12" viewBox="0 0 24 24"><path fill="#fff" d="M6.6 10.8a15 15 0 006.6 6.6l2.2-2.2c.3-.3.7-.4 1-.2 1.1.4 2.3.6 3.6.6.6 0 1 .4 1 1V20c0 .6-.4 1-1 1A17 17 0 013 4c0-.6.4-1 1-1h3.5c.6 0 1 .4 1 1 0 1.3.2 2.5.6 3.6.1.3 0 .7-.2 1z"/></svg>555.014.5800</span>
  <span><svg width="12" height="12" viewBox="0 0 24 24"><path fill="#fff" d="M6 3h12v5H6zM4 9h16a2 2 0 012 2v6h-4v4H6v-4H2v-6a2 2 0 012-2zm4 6v4h8v-4z"/></svg>555.014.1400</span>
  <span><svg width="13" height="10" viewBox="0 0 26 20"><rect x="1" y="1" width="24" height="18" fill="none" stroke="#fff" stroke-width="2"/><path d="M1 1l12 10L25 1" fill="none" stroke="#fff" stroke-width="2"/></svg>info@verdellchiro.com</span>
  <span class="social">PW &nbsp; Chirply</span>
</div>
<div class="abs brand"><span class="mark"></span>Verdell Chiropractic</div>
<nav class="abs nav"><span>Home</span><span>Meet Dr. Harlow</span><span>Testimonials</span><span>FAQs</span><span>Resources</span><span>Contact</span></nav>
<div class="abs cta">Make an Appointment</div>

<!-- hero -->
<div class="abs hero" role="img" aria-label="Chiropractor adjusting a patient's back"></div>
<div class="abs center hero-title">VERDELL CHIROPRACTIC</div>
<div class="abs hero-sub">LOREM IPSUM IS SIMPLY DUMMY TEXT OF THE PRINTING INDUSTRY</div>
<div class="abs center dots" style="top:482px"><i></i><i></i><i></i></div>

<!-- about -->
<h2 class="abs heading about-title">ABOUT US</h2>
<p class="abs about-lead">Health is a process, it does not just happen. We take steps to achieve what we want in life including health.</p>
<p class="abs about-body">Dr. Harlow has over 20 years of experience in chiropractic medicine. He has pursued post graduate work in acupunture, applied kinesiology, nutrition, herbology, and homeopathy. His main goal is to get you well, and he has many tools at his disposal to accomplish this goal.</p>
<div class="abs btn-outline about-btn">Read More</div>
<div class="abs about-photo" role="img" aria-label="Doctor explaining a spine model to a patient"></div>

<!-- conditions -->
<section class="abs conditions"></section>
<h2 class="abs center heading light" style="top:1062px">CONDITIONS</h2>
<p class="abs center cond-intro">It is a long established fact that a reader will be distracted by the readable content of a page when looking at its layout.</p>
<div class="abs cond-grid">
  <div class="cond-tile"><div class="ph" role="img" aria-label="Person with a headache" style="background:linear-gradient(135deg,#8a7a6c,#d7c4b1)"></div><p>HEADACHES</p></div>
  <div class="cond-tile"><div class="ph" role="img" aria-label="Person holding a painful shoulder" style="background:linear-gradient(135deg,#b5473c,#e0b59c)"></div><p>SHOULDER PAIN</p></div>
  <div class="cond-tile"><div class="ph" role="img" aria-label="Hands on the lower back" style="background:linear-gradient(135deg,#a8735a,#e5c0a6)"></div><p>LOWER BACK PAIN</p></div>
  <div class="cond-tile"><div class="ph" role="img" aria-label="Knee being held" style="background:linear-gradient(135deg,#c84a3e,#d9dde0)"></div><p>KNEE PAIN</p></div>
  <div class="cond-tile"><div class="ph" role="img" aria-label="Person in pain from fibromyalgia" style="background:linear-gradient(135deg,#2b2b2b,#b98a70)"></div><p>FIBROMYALGIA</p></div>
  <div class="cond-tile"><div class="ph" role="img" aria-label="Person holding a sore neck" style="background:linear-gradient(135deg,#c79a76,#efe2d3)"></div><p>NECK PAIN</p></div>
  <div class="cond-tile"><div class="ph" role="img" aria-label="Person holding a painful wrist" style="background:linear-gradient(135deg,#3f3f44,#c9c3bd)"></div><p>WRIST PAIN</p></div>
  <div class="cond-tile"><div class="ph" role="img" aria-label="Person holding the hip and leg" style="background:linear-gradient(135deg,#d2402f,#4f7fb0)"></div><p>HIP &amp; LEG PAIN</p></div>
  <div class="cond-tile"><div class="ph" role="img" aria-label="Hands on a sore heel" style="background:linear-gradient(135deg,#6b2f2a,#c7463c)"></div><p>HEEL PAIN</p></div>
  <div class="cond-tile"><div class="ph" role="img" aria-label="Diagram of a bulging spinal disc" style="background:linear-gradient(135deg,#ffffff,#e2d2b0)"></div><p>DISC BULGE</p></div>
</div>

<!-- services -->
<h2 class="abs center heading" style="top:1645px">OUR SERVICES</h2>
<p class="abs center tagline services-tag">Contrary to popular belief, Lorem Ipsum is not simply random text.</p>
<div class="abs svc" style="left:90px"><svg width="60" height="52" viewBox="0 0 60 52"><rect x="6" y="34" width="48" height="6" fill="#2f7fc1"/><rect x="10" y="40" width="4" height="10" fill="#2f7fc1"/><rect x="46" y="40" width="4" height="10" fill="#2f7fc1"/><circle cx="22" cy="10" r="6" fill="#2f7fc1"/><rect x="18" y="18" width="10" height="14" fill="#2f7fc1"/><rect x="30" y="26" width="22" height="7" rx="3" fill="#8dc63f"/></svg>CHIROPRACTIC</div>
<div class="abs svc" style="left:238px"><svg width="60" height="52" viewBox="0 0 60 52"><rect x="4" y="38" width="52" height="6" fill="#8dc63f"/><rect x="8" y="44" width="4" height="8" fill="#8dc63f"/><rect x="48" y="44" width="4" height="8" fill="#8dc63f"/><rect x="10" y="30" width="40" height="7" rx="3" fill="#2f7fc1"/><circle cx="32" cy="10" r="6" fill="#2f7fc1"/><rect x="28" y="17" width="9" height="12" fill="#2f7fc1"/></svg>ACUPUNCTURE</div>
<div class="abs svc" style="left:385px"><svg width="60" height="52" viewBox="0 0 60 52"><rect x="6" y="38" width="48" height="6" fill="#8dc63f"/><rect x="12" y="30" width="36" height="7" rx="3" fill="#2f7fc1"/><circle cx="26" cy="8" r="6" fill="#2f7fc1"/><path d="M22 15h9l6 14h-7z" fill="#2f7fc1"/></svg>APPLIED<br>KINESIOLOGY</div>
<div class="abs svc" style="left:530px"><svg width="60" height="52" viewBox="0 0 60 52"><rect x="8" y="34" width="44" height="7" rx="3" fill="#2f7fc1"/><circle cx="30" cy="16" r="6" fill="#2f7fc1"/><path d="M26 23h8l4 10h-16z" fill="#2f7fc1"/><rect x="6" y="42" width="48" height="4" fill="#8dc63f"/></svg>MASSAGE</div>
<div class="abs svc" style="left:677px"><svg width="60" height="52" viewBox="0 0 60 52"><rect x="22" y="2" width="16" height="8" fill="#8dc63f"/><rect x="16" y="10" width="28" height="40" rx="4" fill="#2f7fc1"/><g fill="#fff"><circle cx="24" cy="22" r="2.5"/><circle cx="30" cy="22" r="2.5"/><circle cx="36" cy="22" r="2.5"/><circle cx="27" cy="29" r="2.5"/><circle cx="33" cy="29" r="2.5"/><circle cx="24" cy="36" r="2.5"/><circle cx="30" cy="36" r="2.5"/><circle cx="36" cy="36" r="2.5"/></g></svg>HOMEOPATHY</div>
<div class="abs svc" style="left:822px"><svg width="60" height="52" viewBox="0 0 60 52"><circle cx="30" cy="26" r="24" fill="#2f7fc1"/><g fill="#8dc63f"><rect x="25" y="6" width="10" height="7" rx="2"/><rect x="25" y="16" width="10" height="7" rx="2"/><rect x="25" y="26" width="10" height="7" rx="2"/><rect x="25" y="36" width="10" height="7" rx="2"/></g></svg>SPINAL<br>DECOMPRESSION<br>THERAPY</div>
<div class="abs svc" style="left:970px"><svg width="60" height="52" viewBox="0 0 60 52"><circle cx="28" cy="28" r="20" fill="none" stroke="#2f7fc1" stroke-width="5"/><circle cx="28" cy="28" r="7" fill="#2f7fc1"/><path d="M46 4v12M40 10h12" stroke="#8dc63f" stroke-width="4"/></svg>OTHER<br>SERVICES</div>

<!-- testimonial -->
<div class="abs testimonial" role="img" aria-label="Group of smiling adults walking outdoors among trees"></div>
<div class="abs center quote-mark">“</div>
<p class="abs quote">I am an M.D., and advised many of my patients to consult with Dr. Harlow. Those who took my advice got better quickly. I, personally, have used Dr. Harlow's services on numerous occasions, have always found relief for my conditions, and have saved hundreds of dollars, which otherwise would have been spent on medications that might have had adverse side effects.</p>
<p class="abs center quote-by">R.K.T., M.D., Brookfield TX</p>
<div class="abs center dots" style="top:2308px"><i></i><i></i><i></i></div>

<!-- blog -->
<h2 class="abs center heading" style="top:2472px">LATEST BLOG</h2>
<p class="abs center tagline blog-tag">Contrary to popular belief, Lorem Ipsum is not simply random text.</p>
<article class="abs card" style="left:86px">
  <div class="ph" role="img" aria-label="Chiropractor treating a patient on a table" style="background:linear-gradient(135deg,#f2efe9,#b7a08a)"><div class="date">23rd<br>Aug</div></div>
  <h3>Lorem ipsum is simply dummy</h3>
  <p>Contrary to popular belief, Lorem Ipsum is not simply random text. It has roots in a piece of classical Latin literature from 45 BC, making it over 2000 years old.</p>
  <div class="btn-outline">Read More</div>
</article>
<article class="abs card" style="left:437px">
  <div class="ph" role="img" aria-label="Lower back with highlighted area of pain" style="background:radial-gradient(circle at 50% 60%,#c8262b,#2a2a2a 70%)"><div class="date">23rd<br>Aug</div></div>
  <h3>Lorem ipsum is simply dummy</h3>
  <p>Contrary to popular belief, Lorem Ipsum is not simply random text. It has roots in a piece of classical Latin literature from 45 BC, making it over 2000 years old.</p>
  <div class="btn-outline">Read More</div>
</article>
<article class="abs card" style="left:789px">
  <div class="ph" role="img" aria-label="Doctor consulting with a laptop at a desk" style="background:linear-gradient(135deg,#e9edf1,#8a86b8 60%,#c9ccd2)"><div class="date">23rd<br>Aug</div></div>
  <h3>Lorem ipsum is simply dummy</h3>
  <p>Contrary to popular belief, Lorem Ipsum is not simply random text. It has roots in a piece of classical Latin literature from 45 BC, making it over 2000 years old.</p>
  <div class="btn-outline">Read More</div>
</article>

<!-- footer -->
<footer class="abs footer"></footer>
<div class="abs foot-brand"><span class="mark"></span>Verdell Chiropractic</div>
<div class="abs vline" style="left:355px"></div>
<div class="abs vline" style="left:695px"></div>
<div class="abs foot-h" style="left:430px;top:3106px">SITEMAP</div>
<div class="abs foot-list" style="left:430px;top:3124px">Home<br>Meet Dr. Harlow<br>Testimonials</div>
<div class="abs foot-list" style="left:554px;top:3124px">FAQs<br>Resources<br>Contact</div>
<div class="abs foot-h" style="left:770px;top:3106px">CONTACT INFO</div>
<div class="abs foot-list" style="left:770px;top:3124px;width:200px;line-height:16px"><span style="color:#8dc63f">●</span> Lyle Harlow DC PA, 4410 Meridian Way</div>
<div class="abs foot-list" style="left:770px;top:3168px"><span style="color:#8dc63f">■</span> info@verdellchiro.com</div>
<div class="abs foot-list" style="left:1018px;top:3128px"><span style="color:#8dc63f">●</span> 555.014.5800</div>
<div class="abs foot-list" style="left:1018px;top:3160px"><span style="color:#8dc63f">■</span> 555.014.1400</div>
<div class="abs bottombar"><span>Copyright 2018 &nbsp;|&nbsp; All Rights Reserved</span><span class="social"><span>PW</span><span>Chirply</span></span></div>

</body>
</html>
```